" A empresa funciona com atendimento de consultorio nas áreas de pneumologia e cirurgia toracica - relacionadas às doenças respiratorias. Realizamos também exames de capacidade respiratoria e problemas de sono. Também fazemos atendimento hospitalar e domiciliar, quando solicitado. "

```html
<!DOCTYPE html>
<html lang="pt-BR">
<head>
<meta charset="utf-8">
<title>Pulmora – Papel timbrado</title>
<link rel="stylesheet" href="https://fonts.googleapis.com/css2?family=Montserrat:wght@400;600&display=swap">
<style>
  :root {
    --backdrop: #e6e7e8;
    --paper: #ffffff;
    --brand-dark: #1f4658;
    --brand-blue: #2a9fd6;
    --brand-navy: #233a4d;
    --rule-blue: #7fb8de;
    --text-grey: #8a9096;
  }
  html, body {
    margin: 0;
    width: 1200px;
    height: 1200px;
    overflow: hidden;
    background: var(--backdrop);
    font-family: "Montserrat", sans-serif;
  }
  .letterhead {
    position: absolute;
    left: 211px;
    top: 50px;
    width: 778px;
    height: 1100px;
    background: var(--paper);
    box-shadow: 0 4px 18px rgba(0,0,0,0.12);
  }
  .top-rule {
    position: absolute;
    left: 40px;
    top: 50px;
    width: 420px;
    height: 1px;
    background: var(--rule-blue);
  }
  .side-rule {
    position: absolute;
    right: 40px;
    top: 115px;
    width: 1px;
    height: 860px;
    background: var(--rule-blue);
  }
  .brand-block {
    position: absolute;
    left: 460px;
    top: 20px;
    width: 278px;
    height: 95px;
    background: var(--brand-dark);
    display: flex;
    align-items: center;
    padding-left: 30px;
    box-sizing: border-box;
    gap: 12px;
  }
  .brand-dot {
    width: 22px;
    height: 22px;
    border-radius: 50%;
    background: var(--brand-blue);
    flex: none;
  }
  .brand-name {
    color: #ffffff;
    font-weight: 400;
    font-size: 34px;
    letter-spacing: 1px;
    line-height: 1;
  }
  .brand-tagline {
    color: #ffffff;
    font-weight: 400;
    font-size: 9px;
    margin-top: 6px;
    letter-spacing: 0.5px;
  }
  .footer-bars {
    position: absolute;
    left: 0;
    bottom: 60px;
  }
  .contact {
    position: absolute;
    right: 60px;
    bottom: 62px;
    text-align: right;
    color: var(--text-grey);
    font-size: 10px;
    line-height: 1.55;
  }
</style>
</head>
<body>
  <main class="letterhead">
    <div class="top-rule"></div>
    <div class="side-rule"></div>

    <header class="brand-block">
      <span class="brand-dot"></span>
      <div>
        <div class="brand-name">Pulmora</div>
        <div class="brand-tagline">pneumologia e cirurgia torácica</div>
      </div>
    </header>

    <svg class="footer-bars" width="420" height="50" viewBox="0 0 420 50" aria-hidden="true">
      <defs>
        <linearGradient id="barBlue" x1="0" x2="1">
          <stop offset="0" stop-color="#2a9fd6"/>
          <stop offset="1" stop-color="#5fc0ea"/>
        </linearGradient>
      </defs>
      <polygon points="0,6 330,6 324,14 0,14" fill="url(#barBlue)"/>
      <polygon points="0,28 400,28 392,40 0,40" fill="var(--brand-navy)"/>
    </svg>

    <address class="contact">
      Rua das Palmeiras, 000 - Centro<br>
      (00) 0000-0000<br>
      contato@pulmora.com.br<br>
      www.pulmora.com.br
    </address>
  </main>
</body>
</html>
```